Residential Roofing Company

Website for Residential roofing company. Servicing Minnesota (Hennepin, Anoka, Sherburne County). Located in Ramsey, Minnesota. Asphalt Shingles (KLT and Darvell Pike Manufacturers)

Target Market(s)

Storm Damage repair. Roof Replacement and Repair.

Industry/Entity Type

Residential Roofing

Coding

Coded - Design and coding required

Number of Pages Required

5+ page

Colors

Designer to choose colors to be used in the design.

Requirements
Should not have
• No Commercial Roofing

```html
<!DOCTYPE html>
<html lang="en">
<head>
<meta charset="utf-8">
<title>Halvern Roofing – Residential Roofing</title>
<link rel="stylesheet" href="https://fonts.googleapis.com/css2?family=Montserrat:wght@400;500;600;700;800&display=swap">
<style>
:root{
  --blue:#1f4196;
  --navy:#14306f;
  --ink:#1b1b1b;
  --muted:#4a4a4a;
  --grey:#efefef;
  --panel:#4d4b4b;
  --white:#ffffff;
  --line:#d8d8d8;
}
*{box-sizing:border-box;margin:0;padding:0}
html,body{width:1200px;height:4692px;overflow:hidden}
body{font-family:"Montserrat",sans-serif;color:var(--ink);background:var(--white);position:relative}
.abs{position:absolute}
/* top bar */
.topbar{top:0;left:0;width:1200px;height:40px;background:var(--grey);font-size:12px;color:var(--muted);display:flex;align-items:center;gap:28px;padding-left:168px}
.topbar span{display:flex;align-items:center;gap:6px}
/* nav */
.nav{top:40px;left:0;width:1200px;height:80px;display:flex;align-items:center;padding:0 168px}
.brand{display:flex;align-items:center;gap:10px;font-weight:800;font-size:26px;color:var(--blue);letter-spacing:1px}
.brand i{display:block;width:14px;height:14px;background:var(--blue)}
.menu{margin-left:auto;display:flex;gap:34px;font-size:12px;font-weight:700;text-transform:uppercase}
.menu a{color:var(--ink);text-decoration:none}
.menu a.active{color:var(--blue);border-bottom:2px solid var(--blue);padding-bottom:4px}
.call{margin-left:34px;background:var(--blue);color:var(--white);font-weight:700;font-size:13px;padding:10px 22px;display:flex;gap:8px;align-items:center}
/* hero */
.hero{top:120px;left:0;width:1200px;height:440px;background:linear-gradient(160deg,#7a8a5a 0%,#5d7344 35%,#8a8272 60%,#4e6a3a 100%)}
.hero-card{position:absolute;left:780px;top:80px;width:300px;padding:28px 26px;background:rgba(255,255,255,.92)}
.hero-card h1{font-size:38px;font-weight:800;color:var(--blue);line-height:1.05}
.hero-card p{font-size:13px;margin-top:16px;line-height:1.5}
.arrow{position:absolute;width:30px;height:46px;background:var(--blue);display:flex;align-items:center;justify-content:center}
/* about */
.about{top:560px;left:0;width:1200px;height:700px;background:linear-gradient(135deg,var(--navy),var(--blue));color:var(--white)}
.about-title{position:absolute;left:168px;top:100px;width:460px;font-size:24px;font-weight:800;line-height:1.35;text-transform:uppercase}
.about-text{position:absolute;left:168px;top:290px;width:470px;font-size:12.5px;line-height:1.7;opacity:.9}
.stat{position:absolute;top:528px}
.stat b{display:block;font-size:32px;font-weight:700}
.stat span{font-size:13px;opacity:.9}
.quote{position:absolute;left:688px;top:-12px;width:360px;height:530px;background:var(--panel);padding:30px 40px;color:var(--white)}
.quote-title{font-size:17px;font-weight:700}
.quote-lead{font-size:13px;margin:18px 0 16px;line-height:1.5;opacity:.9}
.field{height:36px;border:1px solid #9a9a9a;margin-bottom:14px;font-size:12px;padding:10px 12px;color:#ddd}
.field.tall{height:90px}
.btn-get{display:inline-block;background:var(--white);color:var(--ink);font-size:11px;font-weight:700;padding:10px 14px;margin-top:4px}
/* services */
.svc-head{top:1330px;left:168px;font-size:24px;font-weight:800}
.svc-intro{top:1320px;left:608px;width:430px;font-size:14px;line-height:1.6}
.svc{position:absolute;left:168px;width:864px;height:308px;display:flex;box-shadow:0 4px 16px rgba(0,0,0,.1)}
.svc .ph{width:380px;height:100%}
.svc .txt{flex:1;background:var(--white);padding:50px 40px}
.svc h4{font-size:16px;font-weight:700;margin:14px 0 12px}
.svc p{font-size:12.5px;line-height:1.6;color:var(--muted)}
/* video */
.video{top:2480px;left:0;width:1200px;height:560px;background:linear-gradient(180deg,#d79a5a 0%,#9a6a4c 30%,#4a3b38 60%,#2f2b2d 100%)}
.play{position:absolute;left:570px;top:250px;width:60px;height:60px;border:3px solid var(--white);border-radius:50%}
/* why */
.why{top:3040px;left:0;width:1200px;height:720px;background:var(--grey)}
.why-title{position:absolute;top:80px;width:1200px;text-align:center;font-size:34px;font-weight:500;line-height:1.3}
.why-lead{position:absolute;top:206px;left:300px;width:600px;text-align:center;font-size:14px;line-height:1.6}
.checks{position:absolute;left:168px;top:312px;width:864px;height:368px;background:var(--white);border-radius:16px;padding:50px 50px;display:grid;grid-template-columns:1fr 1fr;gap:18px 40px;align-content:start}
.checks li{list-style:none;display:flex;gap:12px;font-size:12.5px;line-height:1.4;align-items:flex-start}
.checks svg{flex:none;margin-top:1px}
/* cta */
.cta{top:3760px;left:0;width:1200px;height:260px;background:var(--blue);color:var(--white);text-align:center}
.cta h2{margin-top:56px;font-size:32px;font-weight:800;line-height:1.25}
.cta .btn{display:inline-flex;gap:10px;align-items:center;background:var(--white);color:var(--blue);padding:10px 20px;margin-top:24px;text-align:left}
.cta .btn b{display:block;font-size:14px}
.cta .btn small{font-size:10px;color:var(--muted)}
/* projects */
.proj-title{top:4140px;width:1200px;text-align:center;font-size:26px;font-weight:800}
.proj{position:absolute;top:4200px;width:300px;height:250px}
.dots{top:4500px;left:580px;display:flex;gap:10px}
.dots i{width:8px;height:8px;border-radius:50%;background:var(--navy);opacity:.4}
.dots i:first-child{opacity:1}
.footer{top:4640px;left:0;width:1200px;height:52px;background:var(--navy);color:#cfd6ea;font-size:10px;text-align:center;padding-top:12px;line-height:1.6}
</style>
</head>
<body>

<div class="abs topbar">
  <span><svg width="12" height="10" viewBox="0 0 12 10"><rect x=".5" y=".5" width="11" height="9" fill="none" stroke="#1f4196"/><path d="M.5 .5 6 5l5.5-4.5" fill="none" stroke="#1f4196"/></svg>info@halvernroofing.com</span>
  <span><svg width="10" height="12" viewBox="0 0 10 12"><path d="M5 11S1 6.5 1 4a4 4 0 0 1 8 0c0 2.5-4 7-4 7z" fill="#1f4196"/></svg>Cedar Loop, MN 55000</span>
  <span><svg width="11" height="11" viewBox="0 0 12 12"><path d="M2 1l3 0 1 3-2 1a7 7 0 0 0 3 3l1-2 3 1v3c-6 0-9-3-9-9z" fill="#1f4196"/></svg>(612) 555-0148</span>
</div>

<header class="abs nav">
  <div class="brand"><i></i>HALVERN</div>
  <nav class="menu"><a class="active" href="#">Home</a><a href="#">About</a><a href="#">Service</a><a href="#">Project</a></nav>
  <div class="call"><svg width="12" height="12" viewBox="0 0 12 12"><path d="M2 1l3 0 1 3-2 1a7 7 0 0 0 3 3l1-2 3 1v3c-6 0-9-3-9-9z" fill="#fff"/></svg>CALL</div>
</header>

<section class="abs hero" role="img" aria-label="Aerial photo of a suburban neighbourhood with shingled rooftops among trees">
  <div class="hero-card">
    <h1>LEADERS IN QUALITY ROOFING</h1>
    <p>Residential Roof Repair, Replacement and Storm Damage Contractors in Anoka County and surrounding areas!</p>
  </div>
  <div class="arrow" style="left:140px;top:200px"><svg width="10" height="14"><path d="M8 1 2 7l6 6" fill="none" stroke="#fff" stroke-width="2"/></svg></div>
  <div class="arrow" style="left:1030px;top:200px"><svg width="10" height="14"><path d="M2 1l6 6-6 6" fill="none" stroke="#fff" stroke-width="2"/></svg></div>
</section>

<section class="abs about">
  <h2 class="about-title">Providing quality roofing in Anoka Country and surrounding with over 40 years</h2>
  <p class="about-text">With over 40 years of experience in servicing the residents of the Twin Cities area, the Halvern Roofing team knows what it takes to get the job done right. We are a second generation roofing company that has crafted a modern touch into our brand. Halvern Roofing is a Woman Owned and Operated Company. We've implemented the knowledge and successful business practices from our history and experience into our brand. Roofing is our history and we strive to make sure our customers receive the best experience possible.</p>
  <div class="stat" style="left:168px"><b>1987</b><span>Year Established</span></div>
  <div class="stat" style="left:358px"><b>1000's</b><span>Satisfied Customers</span></div>
  <form class="quote">
    <h3 class="quote-title">Request A Quote</h3>
    <p class="quote-lead">Fill all information details to consult with us</p>
    <div class="field">Full Name</div>
    <div class="field">Your Email</div>
    <div class="field">Subject</div>
    <div class="field tall">Message</div>
    <span class="btn-get">GET QUOTE</span>
  </form>
</section>

<h2 class="abs svc-head">OUR SERVICE</h2>
<p class="abs svc-intro">Experts in our trade, we offer roof repair and replacement for homes across the county, and our roofing options cater for all types of residential pitched roofs.</p>

<article class="svc" style="top:1452px">
  <div class="ph" role="img" aria-label="Photo of a new suburban house with a grey shingled roof" style="background:linear-gradient(180deg,#cfd8de,#8f8f88 55%,#6f7e4f)"></div>
  <div class="txt">
    <svg width="26" height="26" viewBox="0 0 26 26"><path d="M3 12 13 3l10 9M6 10v13h14V10" fill="none" stroke="#1f4196" stroke-width="2"/></svg>
    <h4>Residential Roofing</h4>
    <p>Experts in our trade, we offer roofing design and installation for family homes, and our roofing options cater for all types of asphalt shingle and pitched roofs.</p>
  </div>
</article>

<article class="svc" style="top:1780px">
  <div class="txt">
    <svg width="26" height="26" viewBox="0 0 26 26"><rect x="3" y="6" width="20" height="16" fill="none" stroke="#1f4196" stroke-width="2"/><path d="M3 12h20M9 6v16" stroke="#1f4196" stroke-width="2"/></svg>
    <h4>Storm Damage / Roof Repair</h4>
    <p>Halvern offers a full array of roofing services for hail and wind damaged homes. From a few missing shingles to a complete tear-off, we work with your insurance claim and make it our business to provide long-lasting warranty solutions for your specific roofing project.</p>
  </div>
  <div class="ph" role="img" aria-label="Photo of a shingled house roof after storm repair" style="background:linear-gradient(180deg,#9bb2c8,#3b4247 45%,#24292d)"></div>
</article>

<article class="svc" style="top:2108px">
  <div class="ph" role="img" aria-label="Photo of a row of townhouses with sided facades" style="background:linear-gradient(180deg,#b9cde0,#b08a63 50%,#6e6a5a)"></div>
  <div class="txt">
    <svg width="26" height="26" viewBox="0 0 26 26"><rect x="4" y="4" width="18" height="18" fill="none" stroke="#1f4196" stroke-width="2"/><path d="M13 4v18M4 13h18" stroke="#1f4196" stroke-width="2"/></svg>
    <h4>Siding / Windows</h4>
    <p>Whether you need new siding installed or if you need help with your insurance claim after a damaging storm. Our dedicated project managers will see to it that you're completely satisfied with your siding and we hope to make the entire process as stress free as possible!</p>
  </div>
</article>

<section class="abs video" role="img" aria-label="Video still of new homes with dark shingled roofs at sunset">
  <div class="play"><svg width="54" height="54" viewBox="0 0 54 54"><path d="M21 16v22l17-11z" fill="#fff"/></svg></div>
</section>

<section class="abs why">
  <h2 class="why-title">Why should you choose Halvern<br>Roofing Services?</h2>
  <p class="why-lead">We take great pride in offering top quality services using high quality materials at very competitive pricing. All of our work is undertaken with a Free Initial Consultation and Quotation, as well as expert advice on your roofing needs.</p>
  <ul class="checks">
    <li><svg width="14" height="14"><circle cx="7" cy="7" r="6.5" fill="none" stroke="#1f4196"/><path d="M4 7l2 2 4-4" fill="none" stroke="#1f4196" stroke-width="1.5"/></svg>Independent roofing company established in 1987</li>
    <li><svg width="14" height="14"><circle cx="7" cy="7" r="6.5" fill="none" stroke="#1f4196"/><path d="M4 7l2 2 4-4" fill="none" stroke="#1f4196" stroke-width="1.5"/></svg>Top quality results every time</li>
    <li><svg width="14" height="14"><circle cx="7" cy="7" r="6.5" fill="none" stroke="#1f4196"/><path d="M4 7l2 2 4-4" fill="none" stroke="#1f4196" stroke-width="1.5"/></svg>Highly skilled and reliable tradesmen with over 40 years of roofing experience</li>
    <li><svg width="14" height="14"><circle cx="7" cy="7" r="6.5" fill="none" stroke="#1f4196"/><path d="M4 7l2 2 4-4" fill="none" stroke="#1f4196" stroke-width="1.5"/></svg>A huge amount of residential storm repair experience and expert advice available</li>
    <li><svg width="14" height="14"><circle cx="7" cy="7" r="6.5" fill="none" stroke="#1f4196"/><path d="M4 7l2 2 4-4" fill="none" stroke="#1f4196" stroke-width="1.5"/></svg>A comprehensive range of roofing services available</li>
    <li><svg width="14" height="14"><circle cx="7" cy="7" r="6.5" fill="none" stroke="#1f4196"/><path d="M4 7l2 2 4-4" fill="none" stroke="#1f4196" stroke-width="1.5"/></svg>Insurance work undertaken</li>
    <li><svg width="14" height="14"><circle cx="7" cy="7" r="6.5" fill="none" stroke="#1f4196"/><path d="M4 7l2 2 4-4" fill="none" stroke="#1f4196" stroke-width="1.5"/></svg>Competitive prices - free quotations</li>
    <li><svg width="14" height="14"><circle cx="7" cy="7" r="6.5" fill="none" stroke="#1f4196"/><path d="M4 7l2 2 4-4" fill="none" stroke="#1f4196" stroke-width="1.5"/></svg>All work is guaranteed</li>
    <li><svg width="14" height="14"><circle cx="7" cy="7" r="6.5" fill="none" stroke="#1f4196"/><path d="M4 7l2 2 4-4" fill="none" stroke="#1f4196" stroke-width="1.5"/></svg>All staff are CSR registered</li>
    <li><svg width="14" height="14"><circle cx="7" cy="7" r="6.5" fill="none" stroke="#1f4196"/><path d="M4 7l2 2 4-4" fill="none" stroke="#1f4196" stroke-width="1.5"/></svg>Fully insured</li>
  </ul>
</section>

<section class="abs cta">
  <h2>DEDICATED TO PROVIDING THE HIGHEST<br>QUALITY ROOFING SERVICES</h2>
  <div class="btn"><svg width="22" height="22" viewBox="0 0 22 22"><circle cx="11" cy="11" r="10" fill="#1f4196"/><path d="M7 6h3l1 3-2 1a5 5 0 0 0 3 3l1-2 3 1v3c-5 0-9-4-9-9z" fill="#fff"/></svg><span><b>MAKE AN ENQUIRY</b><small>We Look Forward To Helping You!</small></span></div>
</section>

<h2 class="abs proj-title">PROJECT</h2>
<div class="proj" style="left:168px;background:linear-gradient(160deg,#6f8a4d,#8c7a62 50%,#5c7a3e)" role="img" aria-label="Aerial photo of a finished house roof among trees"></div>
<div class="proj" style="left:488px;background:linear-gradient(160deg,#7d8f5e,#9b9386 50%,#5f7845)" role="img" aria-label="Aerial photo of a residential street with new roofs"></div>
<div class="proj" style="left:808px;width:224px;background:linear-gradient(160deg,#6a8248,#a08c70 50%,#587340)" role="img" aria-label="Aerial photo of a suburban home roof replacement"></div>
<div class="arrow" style="left:120px;top:4300px"><svg width="10" height="14"><path d="M8 1 2 7l6 6" fill="none" stroke="#fff" stroke-width="2"/></svg></div>
<div class="arrow" style="left:1050px;top:4300px"><svg width="10" height="14"><path d="M2 1l6 6-6 6" fill="none" stroke="#fff" stroke-width="2"/></svg></div>
<div class="abs dots"><i></i><i></i><i></i></div>

<footer class="abs footer">
  Terms of Use &nbsp;|&nbsp; Privacy &amp; Cookie Policy &nbsp;|&nbsp; Trading Terms<br>
  © 2024. The content on this website is owned by us and our licensors. Do not copy any content (including images) without our consent.
</footer>

</body>
</html>
```